Real estate investor business card to retire young ;)!

I need a logo design and a business card. I am based in Montreal, Canada. I buy multi-family properties and do lots development. The final design should communicate that I am a problem solver and reliable.

This card will be given to other investors, to potential sellers and industry experts.

Target Market(s)

Real estate community, multi-family owners

Industry/Entity Type

Real Estate Development

Contact Information for Business Card

My name: Karine Beaulac
email: immo.karine.beaulac@postelune.ca
cellphone: (438) 555-2947

Logo Text

Gestion immobilière

Font styles to use
Sans Serif

Colors
3176b5

Requirements
Must have
• Within 1-2 seconds the person who sees my card should know that I buy properties and lot. Areas to for Phone number and email adress. I do not have a business name. The card should simply state my name and what I do. The logo should be remembered by the person who reads my card
Should not have
• Colors too bright. Too much small details. I want something balanced, bold without being agressive.

```html
<!DOCTYPE html>
<html lang="en">
<head>
<meta charset="utf-8">
<title>Karine Beaulac — Business Card</title>
<link rel="stylesheet" href="https://fonts.googleapis.com/css2?family=Arimo:wght@400&display=swap">
<style>
  :root {
    --page: #ffffff;
    --frame: #232325;
    --card-base: #050a0b;
    --card-mid: #202221;
    --gloss-light: #6a6a6a;
    --gloss-dark: #2f3231;
    --green: #14a04b;
    --gold-text: #f2c12e;
    --gold-light: #f0e2b0;
    --gold-mid: #8a7a5c;
    --bronze: #5a3a1a;
    --steel: #5c5c60;
  }
  html, body {
    margin: 0;
    padding: 0;
    width: 1200px;
    height: 1200px;
    overflow: hidden;
    background: var(--page);
  }
  .canvas { display: block; width: 1200px; height: 1200px; }
  .card-frame { fill: var(--frame); }
  .card-face { fill: var(--card-base); }
  .text-contact, .text-name, .text-tagline, .text-brand {
    font-family: "Arimo", Arial, sans-serif;
    font-weight: 400;
  }
  .text-name { fill: var(--green); font-size: 50px; }
  .text-contact { fill: var(--green); font-size: 40px; }
  .text-tagline { fill: var(--gold-text); font-size: 60px; }
  .text-brand { fill: var(--green); font-size: 84px; }
</style>
</head>
<body>
<svg class="canvas" viewBox="0 0 1932 1932" xmlns="http://www.w3.org/2000/svg">
  <defs>
    <linearGradient id="panel-shade" x1="0" y1="0" x2="0" y2="1">
      <stop offset="0" style="stop-color:var(--card-base)"/>
      <stop offset="1" style="stop-color:var(--card-mid)"/>
    </linearGradient>
    <linearGradient id="gloss" x1="0.3" y1="1" x2="1" y2="0">
      <stop offset="0" style="stop-color:var(--gloss-dark)"/>
      <stop offset="1" style="stop-color:var(--gloss-light)"/>
    </linearGradient>
    <linearGradient id="gold-rule" x1="0" y1="0" x2="1" y2="0">
      <stop offset="0" style="stop-color:var(--card-base)"/>
      <stop offset="0.25" style="stop-color:var(--bronze)"/>
      <stop offset="0.5" style="stop-color:var(--gold-light)"/>
      <stop offset="0.75" style="stop-color:var(--gold-mid)"/>
      <stop offset="1" style="stop-color:var(--card-base)"/>
    </linearGradient>
    <linearGradient id="metal-band" x1="0" y1="0" x2="1" y2="0">
      <stop offset="0" style="stop-color:var(--card-base)"/>
      <stop offset="0.22" style="stop-color:var(--gold-mid)"/>
      <stop offset="0.221" style="stop-color:var(--steel)"/>
      <stop offset="0.5" style="stop-color:var(--card-base)"/>
      <stop offset="0.74" style="stop-color:var(--steel)"/>
      <stop offset="0.741" style="stop-color:var(--gold-mid)"/>
      <stop offset="1" style="stop-color:var(--card-base)"/>
    </linearGradient>
    <clipPath id="face-clip">
      <path d="M545 279 H1460 A40 40 0 0 1 1500 319 V816 A65 65 0 0 1 1435 881 H570 A65 65 0 0 1 505 816 V319 A40 40 0 0 1 545 279 Z"/>
    </clipPath>
    <g id="card-body">
      <rect class="card-frame" x="465" y="243" width="1076" height="673" rx="45"/>
      <path class="card-face" d="M545 279 H1460 A40 40 0 0 1 1500 319 V816 A65 65 0 0 1 1435 881 H570 A65 65 0 0 1 505 816 V319 A40 40 0 0 1 545 279 Z"/>
      <g clip-path="url(#face-clip)">
        <polygon fill="url(#panel-shade)" points="505,279 1500,279 1500,643 1455,643 505,418"/>
        <polygon fill="url(#gloss)" points="818,279 1500,279 1500,438"/>
        <g class="metal-stripe">
          <rect x="520" y="645" width="980" height="10" fill="url(#gold-rule)"/>
          <rect x="520" y="655" width="980" height="45" fill="url(#metal-band)"/>
          <rect x="520" y="700" width="980" height="10" fill="url(#gold-rule)"/>
        </g>
      </g>
    </g>
  </defs>

  <g class="card card-front">
    <use href="#card-body"/>
    <text class="text-name" x="595" y="405">Karine Beaulac</text>
    <text class="text-contact" x="595" y="475">email: immo.karine.beaulac@postelune.ca</text>
    <text class="text-contact" x="595" y="565">cellphone: (438) 555-2947</text>
    <text class="text-tagline" x="1008" y="818" text-anchor="middle">Real estate development</text>
  </g>

  <g class="card card-back" transform="translate(0 814)">
    <use href="#card-body"/>
    <text class="text-brand" x="1003" y="620" text-anchor="middle">Beaulac Development</text>
  </g>
</svg>
</body>
</html>
```